pharmacy bi or tri -fold brochure for 3 pharmacy's

we are looking to promote our pharmacy specialty services, specifically the outreach (or mobile services) services such as daily witness of medication ingestion, in home diabetes program, blood pressure and glucose monitoring, customizing medications into powders and liquids so that they are easier to take, free mobile hearing tests, mobile compression sock and brace fitting. see attached brochure from our competitors. we want something more modern/fresh with images of patients at home being serviced. we will need to tweek the content fro our competitor's . our website is www. brightwell pharmacy.ca which lists our 3 pharmacy locations, our logo etc.

Font styles to use
Sans Serif

Colors
85cae6
0255a3
fbee3f
ffffff

Requirements
Must have
• 8.5" x 11" with consistent color scheme to our website www.brightwellphamacy.ca

```html
<!DOCTYPE html>
<html lang="en">
<head>
<meta charset="utf-8">
<title>Brightwell Pharmacy – Outreach Brochure</title>
<link href="https://fonts.googleapis.com/css2?family=Josefin+Sans:wght@400;600&family=Open+Sans:wght@400;600&display=swap" rel="stylesheet">
<style>
:root{
  --sky:#85cae6;
  --navy:#0255a3;
  --blue:#2a86d1;
  --blue-mid:#3d97da;
  --white:#ffffff;
  --ink:#1d1d1d;
  --paper:#f4f6f8;
  --stage:#1b1b1b;
}
*{margin:0;padding:0;box-sizing:border-box}
html,body{width:913px;height:1200px;overflow:hidden}
body{background:var(--stage);font-family:"Open Sans",Arial,sans-serif;color:var(--ink)}
.spread{position:absolute;left:20px;top:272px;width:873px;height:655px;overflow:hidden;
  background:linear-gradient(135deg,#ffffff 0%,var(--paper) 50%,#e9edf1 100%)}
.abs{position:absolute}
.heading{font-family:"Josefin Sans",Arial,sans-serif}
.photo{position:absolute}
.welcome-title{left:13px;top:161px;font-size:20px;color:var(--white);letter-spacing:.3px;text-shadow:0 1px 2px rgba(0,0,0,.3)}
.body-copy{font-size:7.6px;line-height:9.3px;text-align:justify}
.intro{left:27px;top:255px;width:345px;text-align:left}
.hex-frame{position:absolute;width:105px;height:102px;background:var(--sky);
  clip-path:polygon(25% 0,75% 0,100% 50%,75% 100%,25% 100%,0 50%)}
.hex-frame .photo{left:4px;top:4px;width:97px;height:94px;
  clip-path:polygon(25% 0,75% 0,100% 50%,75% 100%,25% 100%,0 50%)}
.location{position:absolute;left:131px;width:287px}
.location .name{color:var(--navy)}
.licence{left:0;top:620px;width:385px;height:34px;color:var(--white);font-size:7.6px;line-height:9px;
  text-align:center;padding-top:8px;padding-right:30px;text-transform:uppercase}
.outreach-tab{left:436px;top:50px;width:219px;height:50px}
.outreach-title{left:445px;top:63px;font-size:21px;color:var(--white);letter-spacing:.8px}
.outreach-copy{left:449px;top:144px;width:187px}
.cta{left:440px;top:320px;width:192px;text-align:center;color:var(--blue);font-size:13.2px;line-height:14.1px;text-transform:uppercase;letter-spacing:.2px}
.insurance-title{left:655px;top:292px;width:218px;text-align:center;color:var(--blue);font-size:16px;line-height:18px;letter-spacing:.8px}
.insurance-copy{left:675px;top:349px;width:187px;color:var(--white);text-align:justify;text-align-last:right}
.programs-title{left:700px;top:431px;width:161px;text-align:right;color:var(--white);font-size:13px;text-decoration:underline;text-underline-offset:2px}
.program-list{position:absolute;left:680px;top:460px;width:181px;list-style:none;color:var(--white);font-size:7.6px;line-height:11px;text-align:right}
.program-list li::after{content:"";display:inline-block;width:4px;height:4px;border-radius:50%;background:var(--white);margin-left:4px;vertical-align:1px}
</style>
</head>
<body>
<main class="spread">
  <svg class="abs" width="873" height="655" viewBox="0 0 873 655" aria-hidden="true">
    <defs>
      <linearGradient id="blueSweep" x1="0" y1="0" x2="1" y2="1">
        <stop offset="0" stop-color="#5aa9e3"/>
        <stop offset="1" stop-color="#2272c0"/>
      </linearGradient>
      <linearGradient id="bandFill" x1="0" y1="0" x2="1" y2="0">
        <stop offset="0" stop-color="#1f79c6" stop-opacity=".92"/>
        <stop offset="1" stop-color="#3d97da" stop-opacity=".92"/>
      </linearGradient>
      <linearGradient id="roomTone" x1="0" y1="0" x2="1" y2="1">
        <stop offset="0" stop-color="#eef1f3"/>
        <stop offset=".55" stop-color="#cfd6dc"/>
        <stop offset="1" stop-color="#8e98a3"/>
      </linearGradient>
    </defs>
    <!-- right panel sweep -->
    <path d="M873 0 V655 H725 C690 610 650 560 645 470 C640 400 640 330 690 280 C740 235 790 200 812 120 C830 60 850 20 873 0 Z" fill="url(#blueSweep)"/>
    <!-- welcome photo area -->
    <path d="M0 0 H400 L290 225 Q280 242 255 242 H0 Z" fill="url(#roomTone)" role="img" aria-label="Photo: a doctor checking an elderly patient's heart with a stethoscope at home"/>
    <path d="M402 0 L292 226 Q283 244 258 244 H0" fill="none" stroke="var(--blue)" stroke-width="2.5"/>
    <!-- welcome band -->
    <path d="M0 149 H382 L362 203 H0 Z" fill="url(#bandFill)"/>
    <!-- licence band -->
    <path d="M0 620 H385 L365 655 H0 Z" fill="url(#blueSweep)"/>
    <!-- outreach tab -->
    <path d="M436 50 H655 L640 100 H436 Z" fill="url(#blueSweep)"/>
    <!-- insurance tab -->
    <path d="M668 287 H873 V336 H655 Q650 336 652 330 L662 293 Q664 287 668 287 Z" fill="var(--white)"/>
    <!-- top-right photo -->
    <path d="M700 27 H820 Q838 27 850 45 L873 90 V200 L845 250 Q833 266 815 266 H700 Q682 266 672 250 L648 160 Q644 146 648 132 L672 45 Q682 27 700 27 Z" fill="url(#roomTone)" role="img" aria-label="Photo: a nurse holding the hand of a smiling elderly patient in bed"/>
    <!-- bottom-centre photo -->
    <path d="M495 416 H590 Q606 416 615 430 L642 502 Q646 514 642 526 L615 599 Q606 613 590 613 H495 Q479 613 470 599 L446 526 Q442 514 446 502 L470 430 Q479 416 495 416 Z" fill="url(#roomTone)" role="img" aria-label="Photo: a caregiver helping a senior woman stand up from her chair"/>
  </svg>

  <h1 class="abs heading welcome-title">Welcome to Brightwell Pharmacy</h1>
  <p class="abs body-copy intro">We are a group of community based specialty pharmacies across the Lower Mainland aimed at providing the absolute best in patient-centered care. Our pharmacies offer a curated &amp; evolving collection of the latest personal care &amp; wellness products that are innovative, functional and cost effective.</p>

  <div class="hex-frame" style="left:18px;top:297px"><div class="photo" role="img" aria-label="Photo: Eastgate pharmacy storefront" style="background:linear-gradient(160deg,#cfd8e0,#7e93a6)"></div></div>
  <p class="location body-copy" style="top:322px"><span class="name">Eastgate</span> Compounding Pharmacy, Home Health + Hearing Clinic is co-located with ClearPath Medical (family practice &amp; walk-in clinic), the Maple Family Clinic &amp; Unity Health Clinic. There is free underground parking available with an entrance located at 4815 Linden Street (the Aurora condo building).</p>

  <div class="hex-frame" style="left:18px;top:402px"><div class="photo" role="img" aria-label="Photo: Harlow pharmacy building exterior" style="background:linear-gradient(160deg,#dfe4e8,#8d98a2)"></div></div>
  <p class="location body-copy" style="top:415px"><span class="name">Harlow</span> Compounding Pharmacy, Home Health + Hearing Clinic has been serving the Richmond community and Lower Mainland since 1953. The pharmacy is conveniently located across from both Richmond Plaza &amp; Westbrook Skytrain Station, next to the Harbour Bank, in the Riverside Medical Building. We are co-located with over 15 family practice physicians, several specialists as well as a walk-in clinic, and offer free customer parking on the east side of the building.</p>

  <div class="hex-frame" style="left:18px;top:511px"><div class="photo" role="img" aria-label="Photo: Northcrest pharmacy and medical clinic entrance" style="background:linear-gradient(160deg,#d6dde3,#6f8fa4)"></div></div>
  <p class="location body-copy" style="top:532px"><span class="name">Northcrest</span> Compounding Pharmacy, Home Health + Hearing Clinic is co-located with Northshore Medical Clinic, Lifeline Physiotherapy, and Seaside Dental at the corner of Cedar Ave and 9th Street in North Vancouver, a few blocks away from Harbourview Hospital. Free customer parking is available upstairs in marked stalls with entry from the rear alley.</p>

  <p class="abs licence">Harlow, Eastgate &amp; Northcrest compounding pharmacies are licensed<br>by the Provincial Pharmacy Board.</p>

  <h2 class="abs heading outreach-title">Outreach Services</h2>
  <p class="abs body-copy outreach-copy">We understand that some patients may have difficulties in travelling to their pharmacy or physician's offices. Our pharmacists are able to visit patient's homes and answer questions or concerns about their medications via comprehensive medication reviews which encompass both prescription and non-prescription medications, supplements, as well as suggesting dietary/lifestyle changes that can further improve one's health. We will also address how to best take each medication, simplify dosing schedules, and identify any possible dose timing or interaction issues as well.</p>

  <p class="abs cta">Please contact us today to find out how we can work with your physician to produce better health outcomes.</p>

  <h2 class="abs heading insurance-title">Government<br>Insurance Coverage</h2>
  <p class="abs body-copy insurance-copy">Many people qualify for BC government or work/school insurance coverage for many healthcare items ranging from injury or support braces, medications, hearing aids and even compression socks. The process to coverage however, can require lots of paperwork – talk to us about your situation and let us help you save time and money!</p>

  <h3 class="abs programs-title" style="font-weight:400">Health Programs</h3>
  <ul class="program-list">
    <li>Arthritis</li>
    <li>Asthma/COPD</li>
    <li>Bio-identical</li>
    <li>hormones &amp; Healthy</li>
    <li>Aging</li>
    <li>Cholesterol</li>
    <li>Diabetes</li>
    <li>Foot Care</li>
    <li>Hearing Care</li>
    <li>Health and Wellness</li>
    <li>High Blood Pressure</li>
    <li>(Hypertension)</li>
    <li>Nutrition</li>
    <li>Osteoporosis</li>
    <li>Pain management</li>
    <li>Sleep</li>
    <li>Wound Care</li>
  </ul>
</main>
</body>
</html>
```